Ridgeline Outfitters Business Cards

Recently had a logo done with Artfolio and now looking for a business card to go along with it.

Target Market(s)

Ridgeline Outfitters is a weapons dealer. My market will be primarily men, hunting, shooting type.

Industry/Entity Type

Business

Contact Information for Business Card

I selected double sided, but this is not required, single or double is going to be fine. I picture the logo on one side, or perhaps just the circle which contains "RO" with the remaining info on the other side.

Font styles to use
Sans Serif

Requirements
Must have
• My name: Milo Brandt
• Title: Owner
• tel: 612-555-0187
• web: www.ridgelineoutfittersmn.example
Nice to have
• I like the concept of a black business card. I would like to keep the colors monotone, black, grey, white or red. Red is acceptable because it is in the logo. I have also seen cards that are matte black with shiny black as well, perhaps for the logo (or circle RO) part of the logo.
• I will upload a couple of the logos for use, and also an example I just found of the black on black. and some others that have a nice contrast.
Should not have
• lots of colors are not wanted.

```html
<!DOCTYPE html>
<html lang="en">
<head>
<meta charset="utf-8">
<title>Ridgeline Outfitters — Business Cards</title>
<link href="https://fonts.googleapis.com/css2?family=Fira+Sans+Condensed:wght@500;700&family=Open+Sans:wght@400;600&display=swap" rel="stylesheet">
<style>
  :root {
    --backdrop: #3a3a3c;
    --card: #1d1d1f;
    --gloss: #6e6e72;
    --grey: #8a8a8e;
    --white: #f2f2f2;
    --red: #d9221c;
  }
  * { margin: 0; padding: 0; box-sizing: border-box; }
  html, body {
    width: 799px; height: 1200px; overflow: hidden;
    background: var(--backdrop);
  }
  .sheet {
    position: relative; width: 799px; height: 1200px;
  }
  .card {
    position: absolute;
    background: var(--card);
    box-shadow: 0 14px 30px rgba(0,0,0,0.45);
  }

  /* Front */
  .card-front {
    left: 90px; top: 60px; width: 620px; height: 354px;
    display: flex; align-items: center; justify-content: center; gap: 18px;
  }
  .front-mark {
    width: 46px; height: 46px; border-radius: 50%;
    border: 5px solid var(--gloss);
  }
  .front-name {
    font-family: "Fira Sans Condensed", sans-serif;
    font-weight: 700; font-size: 38px; letter-spacing: 1px;
    text-transform: uppercase; color: var(--gloss);
  }

  /* Back */
  .card-back {
    left: 222px; top: 470px; width: 354px; height: 620px;
    display: flex; flex-direction: column; align-items: center;
  }
  .brand {
    margin-top: 62px;
    display: flex; align-items: center; gap: 12px;
  }
  .brand-mark {
    width: 34px; height: 34px; border-radius: 50%;
    border: 4px solid var(--red);
  }
  .brand-name {
    font-family: "Fira Sans Condensed", sans-serif;
    font-weight: 700; font-size: 25px; letter-spacing: 1px;
    text-transform: uppercase; color: var(--red);
  }
  .name-box {
    margin-top: 118px;
    padding: 16px 34px 14px;
    border: 1px solid var(--red);
    text-align: center;
  }
  .person-name {
    font-family: "Fira Sans Condensed", sans-serif;
    font-weight: 700; font-size: 27px; color: var(--white);
    text-transform: uppercase; letter-spacing: 0.5px;
  }
  .person-title {
    font-family: "Open Sans", sans-serif;
    font-size: 14px; color: var(--white); margin-top: 2px;
  }
  .contact {
    margin-top: 36px; text-align: center;
    font-family: "Open Sans", sans-serif; color: var(--white);
    font-size: 15px; line-height: 1.9;
  }
  .red-band {
    position: absolute; left: 0; bottom: 0;
    width: 100%; height: 52px; background: var(--red);
  }
</style>
</head>
<body>
<main class="sheet">
  <section class="card card-front" aria-label="Card front">
    <span class="front-mark"></span>
    <span class="front-name">Ridgeline Outfitters</span>
  </section>

  <section class="card card-back" aria-label="Card back">
    <div class="brand">
      <span class="brand-mark"></span>
      <span class="brand-name">Ridgeline Outfitters</span>
    </div>
    <div class="name-box">
      <p class="person-name">Milo Brandt</p>
      <p class="person-title">Owner</p>
    </div>
    <div class="contact">
      <p class="phone">612-555-0187</p>
      <p class="web">www.ridgelineoutfittersmn.example</p>
    </div>
    <div class="red-band"></div>
  </section>
</main>
</body>
</html>
```